New Web Design Project

Number of Pages Required

1 page

Requirements
Must have
• An Overview / Background of the Business & Services(not for profit rescue animal farm)
• The Target Market / Audience you are trying to reach (animal lovers)
• Design Specifics; any preferences or ideas for Style, Colour, Imagery, etc (no preferences)

```html
<!DOCTYPE html>
<html lang="en">
<head>
<meta charset="utf-8">
<title>Animal Servants</title>
<link href="https://fonts.googleapis.com/css2?family=Courgette&family=Hind:wght@400;600&family=Open+Sans:wght@400&display=swap" rel="stylesheet">
<style>
  :root {
    --page-bg: #f2f2f2;
    --ink: #111111;
    --muted: #6f6f6f;
    --accent: #f0525a;
    --rule: #9a9a9a;
    --dot: #ffffff;
    --plum: #665e69;
    --frame: rgba(255,255,255,0.4);
    --white: #ffffff;
  }
  * { box-sizing: border-box; margin: 0; padding: 0; }
  html, body { width: 1200px; height: 1000px; overflow: hidden; }
  body { background: var(--page-bg); font-family: "Hind", sans-serif; color: var(--ink); position: relative; }

  .section-title {
    position: absolute; left: 0; width: 1200px; text-align: center;
    font-family: "Courgette", cursive; font-size: 47px; line-height: 1; font-weight: 400;
  }
  .title-rule { position: absolute; left: 510px; width: 173px; height: 1px; background: var(--rule); }
  .title-mark { position: absolute; width: 16px; height: 15px; border-radius: 50% 50% 45% 45%; background: var(--ink); }

  .team { position: absolute; left: 0; top: 0; width: 1200px; height: 662px; }
  .team .section-title { top: 21px; color: var(--ink); }

  .member { position: absolute; width: 200px; text-align: center; }
  .avatar {
    display: block; margin: 0 auto; width: 92px; height: 92px; border-radius: 50%;
    border: 4px solid var(--white); box-shadow: 0 0 0 1px #e6e6e6;
  }
  .member-name { margin-top: 20px; font-size: 17px; line-height: 20px; font-weight: 400; }
  .member-name b { font-weight: 600; }
  .member-role { margin-top: 2px; font-family: "Open Sans", sans-serif; font-size: 11px; line-height: 16px; color: var(--accent); }

  .lead { position: absolute; left: 446px; top: 198px; width: 300px; text-align: center; }
  .lead .avatar { width: 238px; height: 238px; border-width: 6px; }
  .lead .member-name { margin-top: 24px; font-size: 19px; }
  .lead-bio { margin: 12px auto 0; width: 290px; font-family: "Open Sans", sans-serif; font-size: 11.6px; line-height: 22.5px; color: var(--muted); }

  .dot-row { position: absolute; top: 333px; height: 10px; }

  .testimonials { position: absolute; left: 0; top: 662px; width: 1200px; height: 338px; background: var(--plum); overflow: hidden; }
  .testimonials-frame { position: absolute; left: 17px; top: 23px; width: 1161px; height: 400px; border: 1px solid var(--frame); }
  .testimonials .section-title { top: 92px; color: var(--white); }
  .testimonials .title-rule { background: var(--white); top: 163px; }
  .testimonials .title-mark { top: 148px; left: 588px; }
  .nav-arrow { position: absolute; top: 258px; width: 38px; height: 38px; border: 1.5px solid var(--white); border-radius: 50%; }
  .nav-arrow svg { display: block; }
  .quote-avatar { position: absolute; left: 561px; top: 239px; width: 68px; height: 68px; border-radius: 50%; border: 3px solid var(--white); background: linear-gradient(135deg, #e9b56a, #f2d3b4 55%, #c98b5c); }
  .quote-badge { position: absolute; left: 606px; top: 288px; width: 26px; height: 26px; border-radius: 50%; background: var(--accent); }
  .quote-author { position: absolute; left: 0; top: 325px; width: 1200px; text-align: center; color: var(--white); font-size: 16px; }
  .quote-author b { font-weight: 600; }
</style>
</head>
<body>

<section class="team">
  <h1 class="section-title">Animal Servants</h1>
  <div class="title-rule" style="top:91px"></div>
  <div class="title-mark" role="img" aria-label="Small cat silhouette" style="left:588px;top:75px"></div>

  <svg class="dot-row" style="left:153px;width:310px" viewBox="0 0 310 10" aria-hidden="true">
    <defs>
      <pattern id="dotsA" width="60" height="10" patternUnits="userSpaceOnUse">
        <circle cx="4" cy="5" r="2" fill="var(--dot)"/>
        <circle cx="16" cy="5" r="2" fill="var(--dot)"/>
        <circle cx="28" cy="5" r="3.4" fill="var(--dot)"/>
        <circle cx="40" cy="5" r="2" fill="var(--dot)"/>
        <circle cx="52" cy="5" r="2" fill="var(--dot)"/>
      </pattern>
    </defs>
    <rect width="310" height="10" fill="url(#dotsA)"/>
  </svg>
  <svg class="dot-row" style="left:730px;width:310px" viewBox="0 0 310 10" aria-hidden="true">
    <rect width="310" height="10" fill="url(#dotsA)"/>
  </svg>

  <div class="member" style="left:119px;top:161px">
    <span class="avatar" role="img" aria-label="Portrait photo of a farm volunteer" style="background:linear-gradient(135deg,#6f8f55,#c9a58a 50%,#4a3a30)"></span>
    <p class="member-name"><b>Milo</b> Granger</p><p class="member-role">Animal Carer</p>
  </div>
  <div class="member" style="left:270px;top:161px">
    <span class="avatar" role="img" aria-label="Portrait photo of a farm volunteer" style="background:linear-gradient(135deg,#3d4f35,#d0a088 50%,#5a4a3c)"></span>
    <p class="member-name"><b>Owen</b> Lefevre</p><p class="member-role">Animal Carer</p>
  </div>
  <div class="member" style="left:721px;top:161px">
    <span class="avatar" role="img" aria-label="Portrait photo of a farm volunteer" style="background:linear-gradient(135deg,#6d93b8,#c99a82 50%,#2c2a30)"></span>
    <p class="member-name"><b>Dorian</b> Ellis</p><p class="member-role">Animal Carer</p>
  </div>
  <div class="member" style="left:872px;top:161px">
    <span class="avatar" role="img" aria-label="Portrait photo of a farm volunteer" style="background:linear-gradient(135deg,#3d4f35,#d0a088 50%,#5a4a3c)"></span>
    <p class="member-name"><b>Ezra</b> Yates</p><p class="member-role">Animal Carer</p>
  </div>
  <div class="member" style="left:119px;top:372px">
    <span class="avatar" role="img" aria-label="Portrait photo of a farm volunteer" style="background:linear-gradient(135deg,#3a2a22,#d19a80 55%,#8a5a44)"></span>
    <p class="member-name"><b>Ethan</b> Ward</p><p class="member-role">Animal Carer</p>
  </div>
  <div class="member" style="left:270px;top:372px">
    <span class="avatar" role="img" aria-label="Portrait photo of a farm volunteer" style="background:linear-gradient(135deg,#c8c3bd,#e0b49c 50%,#7a6a5e)"></span>
    <p class="member-name"><b>Vince</b> Carlow</p><p class="member-role">Animal Carer</p>
  </div>
  <div class="member" style="left:721px;top:372px">
    <span class="avatar" role="img" aria-label="Portrait photo of a farm volunteer" style="background:linear-gradient(135deg,#6f8f55,#c9a58a 50%,#4a3a30)"></span>
    <p class="member-name"><b>Andres</b> Holt</p><p class="member-role">Animal Carer</p>
  </div>
  <div class="member" style="left:872px;top:372px">
    <span class="avatar" role="img" aria-label="Portrait photo of a farm volunteer" style="background:linear-gradient(135deg,#4a4a48,#c79078 55%,#3a3530)"></span>
    <p class="member-name"><b>Benny</b> Pratt</p><p class="member-role">Animal Carer</p>
  </div>

  <div class="lead">
    <span class="avatar" role="img" aria-label="Portrait photo of the farm founder in a park" style="background:linear-gradient(160deg,#cfe0c4,#6f9a5a 45%,#2f8a4a 75%,#3a6a3a)"></span>
    <p class="member-name"><b>Felix</b> Stone</p>
    <p class="member-role">Farm Founder</p>
    <p class="lead-bio">Lorem ipsum dolor sit amet, consectetur adipiscing elit, sed do eiusmod tempor incididunt ut labore et dolore magna aliqua.</p>
  </div>
</section>

<section class="testimonials">
  <div class="testimonials-frame"></div>
  <h2 class="section-title">Customar Says</h2>
  <div class="title-rule"></div>
  <div class="title-mark" role="img" aria-label="Small cat silhouette"></div>

  <div class="nav-arrow" style="left:155px">
    <svg width="35" height="35" viewBox="0 0 35 35" aria-label="Previous"><path d="M19.5 13 L15 17.5 L19.5 22" fill="none" stroke="var(--white)" stroke-width="1.5"/></svg>
  </div>
  <div class="nav-arrow" style="left:999px">
    <svg width="35" height="35" viewBox="0 0 35 35" aria-label="Next"><path d="M15.5 13 L20 17.5 L15.5 22" fill="none" stroke="var(--white)" stroke-width="1.5"/></svg>
  </div>

  <div class="quote-avatar" role="img" aria-label="Portrait photo of a smiling visitor"></div>
  <div class="quote-badge">
    <svg width="26" height="26" viewBox="0 0 26 26" aria-hidden="true">
      <path d="M9 10h3v3.5c0 1.5-.8 2.5-2 3l-.5-.8c.7-.4 1-1 1-1.7H9z M14 10h3v3.5c0 1.5-.8 2.5-2 3l-.5-.8c.7-.4 1-1 1-1.7H14z" fill="var(--white)"/>
    </svg>
  </div>
  <p class="quote-author"><b>Maren</b> Lu</p>
</section>

</body>
</html>
```